Ashgrove Wellness and pain clinic

I will like a leaflet that I have ideas for colours should be tranquil maybe a green or blue. I have the literature
and now need a design for the front of the leaflet again I have some ideas to follow then follow the format of my previous leaflet
Attachment 1 old flyer
Attachment 2/3 idea for front page design
Attachment 4 colour idea or a mutted blue
Attachment 5/6 Ideas for pictures in the leaflet or if you have something better please let me see
Attachment 7 new wording for the inside of the leaflet

Target Market(s)

those who are looking for an alternative to orthodox medicine

Industry/Entity Type

Alternative Medicine

Font styles to use
Script

Colors
cee9f5
87cfc6
cadf82

Requirements
Must have
• Mutted colours. classical design, clear and concise layout
Nice to have
• See attachments but on front page would like the 5 elements of acupuncture and needles. May just a background colour with white text
Should not have
• bright or strong colours the whole leaflet should outline tranqulity

```html
<!DOCTYPE html>
<html lang="en">
<head>
<meta charset="utf-8">
<title>Ashgrove Wellness and pain clinic – Leaflet</title>
<link href="https://fonts.googleapis.com/css2?family=Open+Sans:wght@400;600;700&family=Raleway:wght@300;400&display=swap" rel="stylesheet">
<style>
:root{
  --teal:#3a9e9a;
  --teal-dark:#1f6a70;
  --teal-light:#9fd6cf;
  --sky:#cee9f5;
  --ink:#4a4a4a;
  --paper:#ffffff;
  --bg:#ffffff;
}
*{box-sizing:border-box;margin:0;padding:0}
html,body{width:857px;height:1200px;overflow:hidden;background:var(--bg)}
body{font-family:"Open Sans",Arial,sans-serif;color:var(--ink);position:relative}
.sheet{position:absolute;left:10px;width:837px;background:var(--paper);box-shadow:0 1px 4px rgba(0,0,0,.25);overflow:hidden}
.sheet--outside{top:8px;height:535px}
.sheet--inside{top:563px;height:630px}
.panel{position:absolute;top:0;width:279px;height:100%}
.panel--1{left:0}.panel--2{left:279px}.panel--3{left:558px}
.heading{font-size:10px;font-weight:700;letter-spacing:.5px;color:var(--teal);text-transform:uppercase;margin:0 0 6px}
.body{font-size:6.4px;line-height:1.55;margin-bottom:6px}
.pad{position:absolute;left:18px;right:18px}
.photo{position:absolute}
.band{position:absolute;left:0;width:558px;top:268px;height:267px;background:var(--teal-light)}
.title{font-family:"Raleway",Arial,sans-serif;font-weight:300;color:var(--teal);font-size:32px;line-height:1.05}
.band-text .title{color:#fff}
.list{list-style:none;font-size:6.6px;line-height:1.8}
.list li::before{content:"•";color:var(--teal);margin-right:5px}
.price{display:flex;justify-content:space-between;font-size:6.6px;line-height:1.8}
.dark{background:var(--teal-dark);color:#e8f4f3}
.dark .heading{color:#fff}
.url{position:absolute;left:279px;right:0;bottom:0;height:34px;background:var(--teal);color:#fff;font-size:12px;letter-spacing:1.5px;display:flex;align-items:center;justify-content:center}
.small{font-size:6.4px;line-height:1.6}
</style>
</head>
<body>

<section class="sheet sheet--outside">
  <div class="band"></div>

  <div class="panel panel--1">
    <div class="pad" style="top:20px">
      <h2 class="heading">About Mara</h2>
      <p class="body">Mara trained as a fitness and aerobics instructor in 1986 and has kept working in the health and fitness field ever since then.</p>
      <p class="body">In 1998 she gained a BA Hons degree in Sport and Leisure from a Midlands university. In 1999 she went on to gain a diploma in full body massage, aromatherapy and reflexology.</p>
      <p class="body">Having completed a diploma in the Chinese technique in 1999, she has been running successful clinics and teaching classes across the region.</p>
      <p class="body">She gained her degree in Acupuncture in 2006 and is now a full member of a national professional register.</p>
      <p class="body">Mara finally qualified as a traditional acupuncturist in 2014 and now has clinics in Hollybrook.</p>
    </div>
    <div class="photo" style="left:30px;top:300px;width:219px;height:205px;border-radius:50%;background:radial-gradient(circle,#d8efe9 0%,#b5e1d9 70%,#9fd6cf 100%)" role="img" aria-label="Five elements diagram: wood, fire, earth, metal and water joined in a cycle"></div>
  </div>

  <div class="panel panel--2">
    <div class="pad" style="top:20px">
      <h2 class="heading">Price List</h2>
      <div class="price"><span>First consultation and treatment</span><span>£55</span></div>
      <div class="price"><span>Follow-up treatment</span><span>£45</span></div>
      <div class="price"><span>Cosmetic acupuncture session</span><span>£60</span></div>
      <div class="price"><span>Course of six sessions</span><span>£250</span></div>
      <h2 class="heading" style="margin-top:18px">Clinic Hours</h2>
      <p class="small">Monday: 9am – 5pm<br>Tuesday: 9am – 7pm<br>Wednesday: 10am – 4pm<br>Thursday: 9am – 7pm<br>Friday: 9am – 3pm</p>
      <p class="small" style="margin-top:8px">Ashgrove Wellness, 12 Mill Lane, Hollybrook<br>Tel: 01632 960 418</p>
    </div>
    <div class="pad band-text" style="top:380px">
      <p class="title">Midland Vale<br>Acupuncture</p>
      <p class="small" style="color:#fff;margin-top:10px">01632 960 418<br>hello@midlandvaleacupuncture.co.uk<br>www.midlandvaleacupuncture.co.uk</p>
    </div>
  </div>

  <div class="panel panel--3">
    <div class="photo" style="left:20px;top:20px;width:239px;height:230px;background:linear-gradient(160deg,#f4f6f6,#dfe5e6)" role="img" aria-label="Acupuncture needles fanned out on white"></div>
    <div class="pad" style="top:380px">
      <p class="title">Ashgrove Wellness<br>Hollybrook</p>
      <p class="small" style="margin-top:10px">Mara Linden Lic.Ac. BA (Hons)<br>Dip. Registered Practitioner</p>
      <p class="small" style="margin-top:10px;color:var(--teal)">www.midlandvaleacupuncture.co.uk</p>
    </div>
  </div>
</section>

<section class="sheet sheet--inside">
  <div class="panel panel--1 dark">
    <div class="pad" style="top:20px">
      <h2 class="heading">Cosmetic Acupuncture</h2>
      <p class="body">Cosmetic acupuncture is a gentle, natural way to refresh the face. Fine needles encourage circulation and collagen, softening lines and lifting tired skin without surgery or injections.</p>
      <p class="body">A course of treatments is usually recommended, and each session also works on general health, as the whole body is treated at the same time.</p>
      <p class="body">Many people find the treatment deeply relaxing and notice better sleep, brighter skin and a calmer mood.</p>
      <h2 class="heading" style="margin-top:10px">What to Expect</h2>
      <p class="body">Your first appointment begins with a detailed consultation about your health, lifestyle and diet, followed by treatment. Very fine single-use needles are placed at chosen points and left in place while you rest.</p>
      <p class="body">Most people feel only a light tingle or dull ache. Sessions last around an hour, and a plan is agreed with you to suit your needs.</p>
    </div>
    <div class="photo" style="left:0;top:378px;width:279px;height:252px;background:linear-gradient(135deg,#c9d7d3,#8fa9a6)" role="img" aria-label="Client lying relaxed while receiving facial acupuncture"></div>
  </div>

  <div class="panel panel--2">
    <div class="photo" style="left:0;top:0;width:279px;height:150px;background:linear-gradient(135deg,#6b4a37,#2f2019)" role="img" aria-label="Acupuncture needles placed along a person's back"></div>
    <div class="pad" style="top:165px">
      <h2 class="heading">Acupuncture for Pain</h2>
      <p class="body">Acupuncture can offer real relief from long-term and recent pain. It may reduce swelling, relax tight muscles and help the body release its own natural pain killers.</p>
      <p class="body">It is often used alongside other care and can help reduce reliance on medication for many everyday conditions.</p>
      <h2 class="heading" style="margin-top:10px">What can acupuncture help?</h2>
      <ul class="list">
        <li>Chronic back, neck and knee pain</li>
        <li>Chronic tension headaches and migraine</li>
        <li>Osteoarthritis and fibromyalgia</li>
        <li>IBS and abdominal pain</li>
        <li>Sports injuries and joint strain</li>
        <li>Shoulder and elbow pain</li>
        <li>Post-operative discomfort</li>
      </ul>
      <p class="body" style="margin-top:10px">Please get in touch to discuss your condition before booking your first appointment.</p>
    </div>
  </div>

  <div class="panel panel--3">
    <div class="pad" style="top:20px">
      <h2 class="heading">What is Classical Acupuncture?</h2>
      <p class="body">Classical acupuncture is a system of medicine reaching back over two thousand years. It sees health as a balance of energy, or qi, flowing through channels in the body.</p>
      <p class="body">When this flow is blocked or weak, symptoms appear. Treatment aims to restore balance so the body can heal itself.</p>
      <h2 class="heading" style="margin-top:10px">What can acupuncture treat?</h2>
      <ul class="list">
        <li>Anxiety, stress and depression</li>
        <li>Sleep disorders</li>
        <li>Fertility and hormonal issues</li>
        <li>Digestive problems</li>
        <li>Allergies and hay fever</li>
        <li>Low energy and fatigue</li>
        <li>Menopausal symptoms</li>
        <li>Skin conditions</li>
        <li>Smoking and weight support</li>
      </ul>
      <h2 class="heading" style="margin-top:12px">Testimonial</h2>
      <p class="body" style="font-style:italic">"I began treatment after years of back pain. Within a few sessions I was sleeping well and moving freely. I cannot recommend Mara enough." – Mrs J, Eastbury</p>
    </div>
  </div>

  <div class="url">www.midlandvaleacupuncture.co.uk</div>
</section>

</body>
</html>
```